Contemporary Media Company with Logo Needs Business Card Design

Need a modern card design for a full service digital media company using the logo included. Also want the info below on the card. Probably list the services on the card back to save space for the front. Want something contemporary to impress prospective clients. You may want to submit both a somewhat more conservative design, and then a more wild one.
General Info: (this phrase need not be on the card)
Tod Parvin
Founder and CEO
949-628-4513
tod@lumavantstudio.example
lumavantstudio.example
Services: (this word need not be on the card)
Content & Experience Strategy
Brand Development
Search Engine Optimization
Website Design
Website Operation
Social Media Integration
Complete Video Solutions
Industry/Entity Type
Business
Contact Information for Business Card
Tod Parvin
Founder and CEO
949-628-4513
tod@lumavantstudio.example
lumavantstudio.example
Brand Development
Website Design
Website Operation
Social Media Integration
Complete Video Solutions
Look and feel

```html
<!DOCTYPE html>
<html lang="en">
<head>
<meta charset="utf-8">
<title>Lumavant Studio — Business Card</title>
<link rel="stylesheet" href="https://fonts.googleapis.com/css2?family=Open+Sans:wght@400;600;700&display=swap">
<style>
  :root {
    --backdrop: #e6e3df;
    --card-black: #0b0b0c;
    --card-sheen: #1c1c1e;
    --ink-white: #f4f4f4;
    --ink-grey: #a9a9ab;
    --accent-orange: #f0841e;
    --rule: #d8d8d8;
  }
  * { margin: 0; padding: 0; box-sizing: border-box; }
  html, body {
    width: 1200px; height: 913px; overflow: hidden;
    background: var(--backdrop);
    font-family: "Open Sans", Arial, sans-serif;
  }
  .canvas {
    position: relative; width: 1200px; height: 913px;
    display: flex; align-items: center; justify-content: center; gap: 40px;
  }
  .card {
    position: relative; width: 520px; height: 297px;
    background: linear-gradient(125deg, var(--card-sheen) 0%, var(--card-black) 45%, var(--card-black) 100%);
    box-shadow: 0 18px 40px rgba(0,0,0,0.28);
    overflow: hidden; color: var(--ink-white);
  }
  .brand-name {
    display: flex; align-items: center; gap: 10px;
    font-weight: 400; color: var(--ink-grey);
    letter-spacing: 0.18em; text-transform: uppercase;
  }
  .brand-mark { width: 14px; height: 14px; background: var(--accent-orange); }

  /* Front */
  .card-front .brand-name { position: absolute; left: 34px; top: 112px; font-size: 19px; }
  .holder {
    position: absolute; right: 46px; top: 34px; text-align: right;
  }
  .holder-name { font-size: 19px; font-weight: 700; line-height: 1.15; }
  .holder-title { font-size: 12.5px; font-weight: 600; color: var(--accent-orange); }
  .holder-bar {
    position: absolute; right: 26px; top: 36px; width: 11px; height: 38px;
    background: var(--ink-white);
  }
  .divider {
    position: absolute; left: 34px; right: 26px; top: 176px;
    height: 1px; background: var(--rule);
  }
  .contact-list {
    position: absolute; left: 34px; top: 200px; list-style: none;
    font-size: 12.5px; line-height: 1.6; color: var(--ink-white);
  }
  .contact-list li { display: flex; align-items: center; gap: 8px; }
  .contact-icon { width: 11px; height: 11px; flex: none; }

  /* Back */
  .card-back { display: flex; flex-direction: column; align-items: center; justify-content: center; }
  .card-back .brand-name { font-size: 22px; margin-bottom: 16px; }
  .service-list {
    list-style: none; text-align: center;
    font-size: 12.5px; line-height: 1.35; color: var(--ink-white);
  }
</style>
</head>
<body>
<main class="canvas">
  <section class="card card-front" aria-label="Card front">
    <div class="brand-name"><span class="brand-mark"></span>Lumavant Studio</div>
    <div class="holder">
      <p class="holder-name">Tod Parvin</p>
      <p class="holder-title">Founder and CEO</p>
    </div>
    <span class="holder-bar"></span>
    <span class="divider"></span>
    <ul class="contact-list">
      <li>
        <svg class="contact-icon" viewBox="0 0 12 12" aria-hidden="true"><path d="M2.5 1 4.5 1 5 3.5 3.8 4.4C4.5 6 5.8 7.3 7.4 8L8.3 6.8 11 7.3 11 9.3C11 10.3 10.2 11 9.3 11 4.6 10.7 1.3 7.4 1 2.7 1 1.8 1.6 1 2.5 1Z" fill="var(--accent-orange)"/></svg>
        949-628-4513
      </li>
      <li>
        <svg class="contact-icon" viewBox="0 0 12 12" aria-hidden="true"><rect x="0.8" y="2.3" width="10.4" height="7.4" fill="none" stroke="var(--accent-orange)" stroke-width="1.2"/><path d="M1 2.6 6 6.6 11 2.6" fill="none" stroke="var(--accent-orange)" stroke-width="1.2"/></svg>
        tod@lumavantstudio.example
      </li>
      <li>
        <svg class="contact-icon" viewBox="0 0 12 12" aria-hidden="true"><g fill="none" stroke="var(--accent-orange)" stroke-width="1"><circle cx="6" cy="6" r="5"/><ellipse cx="6" cy="6" rx="2.2" ry="5"/><path d="M1 6H11M2 3.3H10M2 8.7H10"/></g></svg>
        www.lumavantstudio.example
      </li>
    </ul>
  </section>

  <section class="card card-back" aria-label="Card back">
    <div class="brand-name"><span class="brand-mark"></span>Lumavant Studio</div>
    <ul class="service-list">
      <li>Content &amp; Experience Strategy</li>
      <li>Brand Development</li>
      <li>Search Engine Optimization</li>
      <li>Website Design</li>
      <li>Website Operation</li>
      <li>Social Media Integration</li>
      <li>Complete Video Solutions</li>
    </ul>
  </section>
</main>
</body>
</html>
```